Landing Page for a new, High Production, farming technology

Brightfield Sprout
We need a single landing page, with an email signup for more information.
We build self-contained, farming boxes out of ISO containers. These containers use hydroponics and LED lighting to provide a year round growing environment for crops. So, you could grow crops anywhere at any time of the year in any environment.
For the purpose of this site, we will be doing split testing between several different themes using different sites and keywords.
This site's focus should be providing our product to people searching for high production farming technology.
We'll be focusing on the following key words: Agriculture, aquaponics, farm, garden, hydroponics, organic food, subsistence farming, urban farming, vertical garden.
Target Market(s)
We are going to be using this page to judge that
Number of Pages Required
1 page
Look and feel
Each slider illustrates characteristics of the customer's brand and the style your logo design should communicate.

```html
<!DOCTYPE html>
<html lang="en">
<head>
<meta charset="utf-8">
<title>Brightfield Sprout — Container Farming</title>
<link href="https://fonts.googleapis.com/css2?family=Raleway:wght@500;600;700;800&family=Lato:wght@400;700&family=Montserrat:wght@400&display=swap" rel="stylesheet">
<style>
:root{
  --green:#a9c98c;
  --green-dark:#8fb673;
  --green-head:#9dc27f;
  --orange:#e9a668;
  --orange-dark:#d88f4f;
  --ink:#2f2f2f;
  --muted:#777;
  --soft:#f2f2f2;
  --white:#fff;
}
*{box-sizing:border-box;margin:0;padding:0}
html,body{width:1200px;height:2329px;overflow:hidden}
body{position:relative;background:var(--white);font-family:'Lato',sans-serif;color:var(--ink)}
.abs{position:absolute}

/* header */
.site-header{left:0;top:0;width:1200px;height:99px;background:#f3f3f3}
.contact-bar{left:575px;top:0;width:625px;height:31px;background:var(--green);border-bottom-left-radius:30px;display:flex;align-items:center;gap:14px;padding-left:44px;font-size:12px;color:var(--ink)}
.contact-bar .item{display:flex;align-items:center;gap:7px}
.contact-bar .dot{width:20px;height:20px;border-radius:50%;background:var(--orange);display:flex;align-items:center;justify-content:center}
.signup-pill{background:var(--orange);border-radius:12px;padding:3px 12px;font-weight:700;font-size:12px;display:flex;gap:6px;align-items:center}
.brand{left:210px;top:28px;display:flex;align-items:center;gap:12px}
.brand .mark{width:36px;height:36px;background:var(--orange);border-radius:4px}
.brand .name{font-family:'Montserrat',sans-serif;font-size:19px;letter-spacing:5px;color:var(--green-dark);text-transform:uppercase}
.main-nav{top:59px;left:543px;display:flex;gap:0;font-family:'Raleway',sans-serif;font-weight:600;font-size:13px;color:#666}
.main-nav a{position:absolute;white-space:nowrap;text-decoration:none;color:inherit}
.main-nav a.active{color:var(--orange)}

/* hero */
.hero-photo{left:0;top:99px;width:1200px;height:500px;background:linear-gradient(160deg,#c96fb8 0%,#d8c7cf 30%,#eee8e0 55%,#9fbf6e 80%,#5f8a3c 100%)}
.quick-contact{left:750px;top:200px;width:239px;height:300px;background:#f4f4f4;border-radius:10px;box-shadow:0 3px 10px rgba(0,0,0,.2);overflow:hidden}
.quick-contact h3{background:var(--green);color:var(--white);font-family:'Raleway',sans-serif;font-weight:800;font-size:19px;line-height:21px;text-align:center;padding:11px 0 9px;text-transform:uppercase}
.quick-contact .field{margin:6px 6px 0;height:29px;background:var(--white);border:1px solid #d8d8d8;border-radius:3px;font-size:9px;color:#888;padding:8px}
.quick-contact .field.message{height:56px}
.quick-contact .submit{display:block;margin:12px auto 0;width:128px;height:30px;border-radius:15px;background:var(--orange);border:1px solid var(--orange-dark);color:var(--white);font-family:'Raleway',sans-serif;font-weight:700;font-size:12px;line-height:28px;text-align:center}
.slider-nav{left:535px;top:564px;width:130px;height:18px}

/* section titles */
.section-title{left:0;width:1200px;text-align:center;font-family:'Raleway',sans-serif;font-weight:700;font-size:27px;color:var(--green-head);text-transform:uppercase}
.divider{left:546px;width:108px;height:14px}

/* about */
.about-photo{left:211px;top:736px;width:331px;height:228px;border-radius:10px;border:3px solid #e5e5e5;background:linear-gradient(180deg,#2a2ab0 0%,#6b5be0 40%,#3f4bb8 70%,#1b2070 100%)}
.about-text{left:584px;top:728px;width:404px;font-size:11.4px;line-height:19px;color:var(--muted)}
.learn-more{left:584px;top:934px;display:flex;align-items:center}
.learn-more .mark{width:24px;height:28px;background:var(--orange);border-radius:3px;margin-right:-4px;position:relative;z-index:1}
.learn-more .btn{background:var(--orange);color:var(--white);font-family:'Raleway',sans-serif;font-weight:700;font-size:12px;border-radius:0 16px 16px 0;padding:9px 18px 9px 14px}

/* benefits */
.benefits{left:0;top:1020px;width:1200px;height:498px;background:var(--soft)}
.benefit{width:300px;text-align:center}
.benefit .num{width:68px;height:68px;border-radius:50%;background:var(--orange);margin:0 auto;color:var(--white);font-family:'Raleway',sans-serif;font-weight:600;font-size:26px;line-height:68px}
.benefit h4{margin-top:21px;font-family:'Raleway',sans-serif;font-weight:700;font-size:12.5px;color:var(--ink);text-transform:uppercase}
.benefit p{margin-top:10px;font-size:11px;line-height:18px;color:var(--muted)}

/* blog */
.blog-card{top:1656px;width:243px;height:285px;background:var(--white);box-shadow:0 1px 4px rgba(0,0,0,.15);overflow:hidden}
.blog-card .photo{height:165px}
.blog-card .date{position:absolute;left:0;top:111px;width:30px;height:44px;background:var(--orange);color:var(--white);text-align:center;font-weight:700;font-size:14px;line-height:18px;padding-top:4px}
.blog-card .date small{display:block;font-size:7px;line-height:8px}
.blog-card h5{margin:16px 10px 0;font-family:'Raleway',sans-serif;font-weight:700;font-size:13px;line-height:19px;color:var(--ink)}
.blog-card p{margin:14px 10px 0;font-size:8.5px;line-height:14px;color:var(--muted)}
.blog-card .corner{position:absolute;right:0;bottom:0}
.carousel-arrow{top:1783px}

/* footer */
.site-footer{left:0;top:1995px;width:1200px;height:334px;background:linear-gradient(180deg,#a9c98c,#9fc181);color:var(--white)}
.footer-brand{left:0;top:48px;width:1200px;display:flex;justify-content:center;align-items:center;gap:16px}
.footer-brand .mark{width:44px;height:44px;background:var(--white);border-radius:4px}
.footer-brand .name{font-family:'Montserrat',sans-serif;font-size:26px;letter-spacing:7px;text-transform:uppercase}
.footer-nav{left:0;top:149px;width:1200px;display:flex;justify-content:center;gap:45px;font-family:'Raleway',sans-serif;font-weight:700;font-size:12px}
.social{left:0;top:188px;width:1200px;display:flex;justify-content:center;gap:6px}
.social span{width:24px;height:24px;border:1.5px solid var(--white);border-radius:50%}
.copyright{left:0;top:235px;width:1200px;text-align:center;font-size:9.5px;letter-spacing:.3px}
.keywords{left:0;top:298px;width:1200px;text-align:center;font-size:12.5px}
</style>
</head>
<body>

<header class="abs site-header">
  <div class="abs contact-bar" style="left:0;position:relative">
  </div>
</header>
<div class="abs contact-bar">
  <div class="item"><span class="dot"><svg width="10" height="10" viewBox="0 0 10 10"><path d="M2 1l2 2-1 1c.6 1.2 1.6 2.2 2.8 2.8l1-1 2 2-1.3 1.2C4.5 8.7 1.3 5.5 1 2.3z" fill="#fff"/></svg></span>555-201-4478</div>
  <div class="item"><span class="dot"><svg width="11" height="8" viewBox="0 0 11 8"><rect x=".5" y=".5" width="10" height="7" fill="none" stroke="#fff"/><path d="M.5.5l5 4 5-4" fill="none" stroke="#fff"/></svg></span>info@brightfieldsprout.com</div>
  <div class="signup-pill"><svg width="11" height="9" viewBox="0 0 11 9"><path d="M0 4.5h7M4.5 1.5l3 3-3 3" stroke="#2f2f2f" stroke-width="1.5" fill="none"/><path d="M7 .5h3.5v8H7" stroke="#2f2f2f" fill="none"/></svg>Signup</div>
</div>
<div class="abs brand"><span class="mark"></span><span class="name">Brightfield Sprout</span></div>
<nav class="abs main-nav">
  <a class="active" style="left:0">HOME</a>
  <a style="left:81px">ABOUT US</a>
  <a style="left:191px">PRODUCT</a>
  <a style="left:295px">BLOG</a>
  <a style="left:376px">CONATC US</a>
</nav>

<section>
  <div class="abs hero-photo" role="img" aria-label="Hydroponic growing room under pink LED lights with a white shipping container farm in front"></div>
  <form class="abs quick-contact">
    <h3>Get a<br>Quick Contact</h3>
    <div class="field" style="margin-top:8px">Name:</div>
    <div class="field">Phone:</div>
    <div class="field">Email:</div>
    <div class="field message">Message:</div>
    <div class="submit">SUBMIT NOW</div>
  </form>
  <svg class="abs slider-nav" viewBox="0 0 130 18">
    <path d="M2 9h20M2 9l5-4M2 9l5 4" stroke="#fff" stroke-width="1.5" fill="none"/>
    <circle cx="38" cy="9" r="5" fill="none" stroke="#fff" stroke-width="1.3"/>
    <circle cx="55" cy="9" r="2.5" fill="#fff"/><circle cx="70" cy="9" r="2.5" fill="#fff"/><circle cx="85" cy="9" r="2.5" fill="#fff"/>
    <path d="M106 9h20M126 9l-5-4M126 9l-5 4" stroke="#fff" stroke-width="1.5" fill="none"/>
  </svg>
</section>

<section>
  <h2 class="abs section-title" style="top:646px">About Us</h2>
  <svg class="abs divider" style="top:683px" viewBox="0 0 108 14"><line x1="0" y1="7" x2="46" y2="7" stroke="#e9a668"/><line x1="62" y1="7" x2="108" y2="7" stroke="#e9a668"/><rect x="48" y="1" width="12" height="12" fill="#e9a668"/></svg>
  <div class="abs about-photo" role="img" aria-label="Rows of seedlings growing under blue LED light strips"></div>
  <p class="abs about-text">Lorem ipsum dolor sit amet, consectetur adipiscing elit. Nunc ac fermentum elit. Proin porta, diam nec sollicitudin auctor, augue felis vestibulum libero, nec pharetra dolor ex ut sem. Etiam vitae orci interdum, rhoncus erat ut, dictum lectus. Phasellus sed molestie est. Phasellus laoreet ullamcorper velit, at scelerisque ante sagittis quis. Vestibulum sit amet accumsan enim, eget facilisis elit. Vivamus tristique sodales risus eget lacinia. Donec vitae urna metus. Morbi sollicitudin vitae diam a mattis. Suspendisse nec odio orci. Phasellus euismod dolor a orci ultricies eleifend. Donec non condimentum orci.</p>
  <div class="abs learn-more"><span class="mark"></span><span class="btn">LEARN MORE</span></div>
</section>

<section class="abs benefits">
  <h2 class="abs section-title" style="top:48px">Product Benifits</h2>
  <svg class="abs divider" style="top:85px" viewBox="0 0 108 14"><line x1="0" y1="7" x2="46" y2="7" stroke="#e9a668"/><line x1="62" y1="7" x2="108" y2="7" stroke="#e9a668"/><rect x="48" y="1" width="12" height="12" fill="#e9a668"/></svg>

  <div class="abs benefit" style="left:163px;top:135px"><div class="num">01</div><h4>All-Weather Construction</h4><p>Steel frame with sainless interior,<br>40' x 8' x 9.6' overall footprint.</p></div>
  <div class="abs benefit" style="left:449px;top:135px"><div class="num">02</div><h4>Automatic Dosing</h4><p>Programmable nutrient &amp; pH dosing<br>for perfect growing conditions.</p></div>
  <div class="abs benefit" style="left:736px;top:135px"><div class="num">03</div><h4>Custom Workbench</h4><p>TIG-welded sainless workbench with<br>integrated seedling growth stage</p></div>
  <div class="abs benefit" style="left:163px;top:301px"><div class="num">04</div><h4>Commercial Volume</h4><p>Thousands of growing sites across<br>256 irrigated vertical towers.</p></div>
  <div class="abs benefit" style="left:449px;top:301px"><div class="num">05</div><h4>High-Efficiency LED Array</h4><p>5:1 red / blue LED lighting optimized<br>for green leafy growth.</p></div>
  <div class="abs benefit" style="left:736px;top:301px"><div class="num">06</div><h4>Insulated Entry</h4><p>Padlock-proof safety door with<br>controlled-environment insulation.</p></div>
</section>

<section>
  <h2 class="abs section-title" style="top:1567px">Our Blog</h2>
  <svg class="abs divider" style="top:1604px" viewBox="0 0 108 14"><line x1="0" y1="7" x2="46" y2="7" stroke="#e9a668"/><line x1="62" y1="7" x2="108" y2="7" stroke="#e9a668"/><rect x="48" y="1" width="12" height="12" fill="#e9a668"/></svg>

  <svg class="abs carousel-arrow" style="left:138px" width="16" height="30" viewBox="0 0 16 30"><path d="M14 2L3 15l11 13" stroke="#aaa" stroke-width="2" fill="none"/></svg>
  <svg class="abs carousel-arrow" style="left:1045px" width="16" height="30" viewBox="0 0 16 30"><path d="M2 2l11 13L2 28" stroke="#aaa" stroke-width="2" fill="none"/></svg>

  <article class="abs blog-card" style="left:211px">
    <div class="photo" role="img" aria-label="Researcher with a tablet beside strawberry growing racks" style="background:linear-gradient(135deg,#7fa35a,#cfd8c4 60%,#eef0ec)"></div>
    <div class="date">09<small>MAY</small></div>
    <h5>Lorem ipsum amet, consectetur adipiscing elit. Aenean velit ligula.</h5>
    <p>porttitor eget vehicula iaculis, amet nisi. Nulla efficitur eros quis nibh facilisis, vel accumsan risus ornare. Nullam pellentesque sit amet lectus eu.</p>
    <svg class="corner" width="28" height="22" viewBox="0 0 28 22"><path d="M28 0v22H0z" fill="#e9a668"/><path d="M19 10v8M15 14h8" stroke="#fff" stroke-width="1.6"/></svg>
  </article>
  <article class="abs blog-card" style="left:478px">
    <div class="photo" role="img" aria-label="Gloved hand holding a seedling with tweezers in a lab" style="background:linear-gradient(135deg,#2e6fb8,#7dc7d8 50%,#c9e3c0)"></div>
    <div class="date">09<small>MAY</small></div>
    <h5>Lorem ipsum amet, consectetur adipiscing elit. Aenean velit ligula.</h5>
    <p>porttitor eget vehicula iaculis, amet nisi. Nulla efficitur eros quis nibh facilisis, vel accumsan risus ornare. Nullam pellentesque sit amet lectus eu.</p>
    <svg class="corner" width="28" height="22" viewBox="0 0 28 22"><path d="M28 0v22H0z" fill="#a9c98c"/><path d="M19 10v8M15 14h8" stroke="#fff" stroke-width="1.6"/></svg>
  </article>
  <article class="abs blog-card" style="left:745px">
    <div class="photo" role="img" aria-label="Gloved hands planting a seedling plug in a grow tray" style="background:linear-gradient(135deg,#3a3a36,#6d7d5a 50%,#cfcfc8)"></div>
    <div class="date">09<small>MAY</small></div>
    <h5>Lorem ipsum amet, consectetur adipiscing elit. Aenean velit ligula.</h5>
    <p>porttitor eget vehicula iaculis, amet nisi. Nulla efficitur eros quis nibh facilisis, vel accumsan risus ornare. Nullam pellentesque sit amet lectus eu.</p>
    <svg class="corner" width="28" height="22" viewBox="0 0 28 22"><path d="M28 0v22H0z" fill="#e9a668"/><path d="M19 10v8M15 14h8" stroke="#fff" stroke-width="1.6"/></svg>
  </article>
</section>

<footer class="abs site-footer" role="img" aria-label="Green-tinted greenhouse backdrop">
  <div class="abs footer-brand"><span class="mark"></span><span class="name">Brightfield Sprout</span></div>
  <nav class="abs footer-nav"><span>HOME</span><span>ABOUT US</span><span>PRODUCT</span><span>BLOG</span><span>CONATC US</span></nav>
  <div class="abs social"><span></span><span></span><span></span><span></span><span></span></div>
  <p class="abs copyright">© COPYRIGHT 2016 BRIGHTFIELD SPROUT. ALL RIGHTS RESERVED.</p>
  <p class="abs keywords">key words: Agriculture, aquaponics, farm, garden, hydroponics, organic food, subsistence farming, urban farming, vertical garden</p>
</footer>

</body>
</html>
```